Website for Sports and Exercise Medicine Doctor with active research in stem cells therapies.

I am a sports and exercise medicine doctor with research interests in the cutting edge areas of biological therapies, most notable stem cells. None of my patients are dying of anything, and most of them come to see me to decrease their pain, so they can get back to what they want to do.

The approach i then take is to decrease their pain and support them to achieve the things they wish to achieve. Most people start at "Just make it stop hurting doc" , but I try to move them towards something more important over time.

I would like the website to be very different to other "Doctor or medical websites" in its look. No pictures of doctors in white coats and no pictures of fit old people smiling. I would potentially like the fist thing seen to be a quote:

"Less pain. Everybody wants it, but what are you going to do, once you've got it?"

(But this is only an idea, I am open to anything)

The website will need a couple of things

1. "Locations" I work
2. "Research" I am involved in
3. "Sort Me out" - Clinical information for people to access
4. "Social" - imbedded twitter and facebook
5. "Blog" - imbedded wordpress blog
6. "Bio" - the usual bio-stuff

The "Sort Me out" - pages I would like to have the functionality as seen in this site http://www.veltarion.com.au/platelet/. I intend to put disease topics into these pages (eg Achilles tehdinopathy, osteoarthritis etc etc etc). Once again I am not wedded to this but something along these lines would be good.

To give you an idea these are some sites I like
http://www.morbanquilt.com/
http://daptrine.com/
http://ovimbera.com.sg/
http://jolvaniketchup.com/
http://www.pilnorwave.com/
http://quadrisel.com/#offering
http://fennikstudio.tv/
http://norvalgate.com/
http://sablethorn.co.uk/#about

Target Market(s)

20-80 year old.
People with tendon injuries
People with osteoarthritis
People interested in stem cells
I will build the site over time to contain information on multiple sporting injuries and musculoskeletal disorders. It will also become a site for the latest on stem cell research particularly in the area of osteoarthritis.

Industry/Entity Type

Medical

Font styles to use
Sans Serif

Colors
ffffff

Requirements
Nice to have
• To give you an idea these are some sites I like
http://daptrine.com/
http://fennikstudio.tv/
http://norvalgate.com/
Should not have
• Pictures of doctors in white coats or old fit people smiling

```html
<!DOCTYPE html>
<html lang="en">
<head>
<meta charset="utf-8">
<title>Dr Lyle Harrow — Sports and Exercise Medicine</title>
<link href="https://fonts.googleapis.com/css2?family=Quattrocento:wght@400;700&family=Arimo:ital,wght@0,400;0,700;1,400&display=swap" rel="stylesheet">
<style>
:root{
  --white:#ffffff;
  --red:#c3172e;
  --navy:#1f2a5a;
  --lime:#84c22d;
  --green:#3bb44a;
  --green-deep:#31a03f;
  --green-dark:#2f983c;
  --bubble:#2a8a36;
  --footer:#8cc63f;
  --yellow:#d6e021;
  --rule:#9fd88a;
  --serif:'Quattrocento', Georgia, serif;
  --sans:'Arimo', Helvetica, Arial, sans-serif;
}
*{margin:0;padding:0;box-sizing:border-box}
html,body{width:1200px;height:1146px;overflow:hidden}
body{position:relative;background:var(--lime);font-family:var(--sans);color:var(--white)}
a{color:inherit;text-decoration:none}
.abs{position:absolute}

/* header */
.site-header{left:154px;top:0;width:891px;height:117px;background:var(--white)}
.nav-link{font-family:var(--serif);color:var(--red);font-size:20px;position:absolute;top:78px;white-space:nowrap}
.brand{position:absolute;left:388px;top:18px;width:150px;text-align:center}
.brand-dot{width:46px;height:46px;border-radius:50%;background:var(--lime);margin:0 auto 12px}
.brand-name{font-family:var(--serif);font-size:19px;color:var(--navy);white-space:nowrap}

/* hero */
.hero{left:0;top:117px;width:1200px;height:394px;background:var(--lime)}
.quote-mark{font-family:var(--sans);font-weight:700;color:var(--red);font-size:104px;line-height:1}
.quote-open{left:256px;top:130px}
.quote-close{left:690px;top:408px}
.headline{left:262px;top:199px;font-family:var(--serif);font-weight:400;font-size:53px;line-height:48px;color:var(--white);white-space:nowrap}
.subline{left:262px;top:300px;font-family:var(--sans);font-size:41px;line-height:44.6px;color:var(--yellow);width:500px}
.hero-image{left:836px;top:209px;width:200px;height:209px;border-radius:6px;background:linear-gradient(160deg,#d62a2f 0%,#b5121c 55%,#7fa82a 100%)}
.social-tab{top:303px;width:41px;height:44px}
.social-tab.one{left:1117px;background:var(--white);border-radius:4px 0 0 4px}
.social-tab.two{left:1158px;background:#9acb57;width:42px}

/* about */
.about{left:0;top:511px;width:1200px;height:308px;background:var(--green)}
.section-title{font-family:var(--serif);font-weight:400;color:var(--red);font-size:22px}
.about-title{left:186px;top:549px}
.about-rule{left:182px;top:580px;width:529px;height:1px;background:var(--rule)}
.portrait{left:184px;top:603px;width:186px;height:167px;background:linear-gradient(160deg,#f1f1f1,#d9dde2)}
.about-text{left:391px;top:605px;width:330px;font-size:15.5px;line-height:19.2px;letter-spacing:0.45px}
.more-link{font-size:12px;display:flex;align-items:center;gap:10px;color:var(--white)}
.more-link svg{width:18px;height:18px}
.about-more{left:393px;top:755px}
.learn-circle{left:775px;top:537px;width:254px;height:254px;border-radius:50%;background:var(--green-deep)}
.learn-title{left:834px;top:596px;font-family:var(--serif);font-weight:400;font-size:22px}
.learn-list{left:834px;top:623px;list-style:none;font-size:16px;line-height:23.5px;color:var(--yellow)}
.learn-list li{padding-left:17px;position:relative}
.learn-list li::before{content:"";position:absolute;left:1px;top:9px;width:7px;height:7px;border-radius:50%;background:var(--green)}

/* tweet + blog */
.news{left:0;top:819px;width:1200px;height:262px;background:var(--green-dark)}
.tweet-bubble{left:246px;top:834px;width:186px;height:186px;border-radius:50%;background:var(--bubble)}
.tweet-tail{left:270px;top:990px}
.tweet-icon{left:260px;top:1025px;width:26px;height:26px;border-radius:50%;background:var(--lime)}
.tweet-title{left:277px;top:875px;font-family:var(--serif);font-weight:400;font-size:20px}
.tweet-text{left:277px;top:902px;width:146px;font-size:13px;line-height:15.5px;color:var(--yellow);letter-spacing:0.3px}
.blog-title{left:509px;top:862px}
.blog-rule{left:509px;top:893px;width:381px;height:1px;background:#9cc43a}
.blog-date{left:509px;top:903px;font-size:12.5px;font-style:italic}
.blog-text{left:509px;top:922px;width:510px;font-size:15.5px;line-height:19.2px;letter-spacing:0.45px}
.blog-more{left:510px;top:1012px}

/* footer */
.site-footer{left:0;top:1081px;width:1200px;height:65px;background:var(--footer)}
.foot-nav{top:1104px;font-size:16px;font-weight:700;color:var(--white);letter-spacing:0.3px;white-space:nowrap}
</style>
</head>
<body>

<header class="abs site-header">
  <a class="nav-link" style="left:121px" href="#">Location</a>
  <a class="nav-link" style="left:223px" href="#">Research</a>
  <a class="nav-link" style="left:327px" href="#">Blog</a>
  <div class="brand">
    <div class="brand-dot"></div>
    <div class="brand-name">Dr Lyle Harrow</div>
  </div>
  <a class="nav-link" style="left:544px;top:76px;font-size:19px" href="#">Sort Me Out</a>
  <a class="nav-link" style="left:678px;top:76px;font-size:19px" href="#">Bio</a>
  <a class="nav-link" style="left:732px;top:76px;font-size:19px" href="#">Social</a>
</header>

<section class="abs hero"></section>
<div class="abs quote-mark quote-open">“</div>
<h1 class="abs headline">LESS PAIN IS LIKE<br>MORE MONEY.</h1>
<p class="abs subline">Everybody wants it, but<br>what are you going to do<br>once you've got it?</p>
<div class="abs quote-mark quote-close">”</div>
<div class="abs hero-image" role="img" aria-label="Photo of a shiny red apple with a leaf"></div>
<a class="abs social-tab one" href="#" aria-label="Follow on social"></a>
<a class="abs social-tab two" href="#" aria-label="Like on social"></a>

<section class="abs about"></section>
<h2 class="abs section-title about-title">ABOUT US</h2>
<div class="abs about-rule"></div>
<div class="abs portrait" role="img" aria-label="Portrait photo of the doctor"></div>
<p class="abs about-text">I am a sports and exercise medicine doctor with research interests in the cutting edge areas of biological therapies, most notable stem cells. None of my patients are dying of anything, and most of them come to see me to decrease their pain, so they can get back to what they want to do</p>
<a class="abs more-link about-more" href="#">More Information
  <svg viewBox="0 0 18 18"><circle cx="9" cy="9" r="9" fill="#fff"/><path d="M7 4.5 11.5 9 7 13.5" stroke="#3bb44a" stroke-width="2" fill="none"/></svg>
</a>
<div class="abs learn-circle"></div>
<h3 class="abs learn-title">Learn More</h3>
<ul class="abs learn-list">
  <li>Sports and Exercise</li>
  <li>Sports and Exercise</li>
  <li>Sports and Exercise</li>
  <li>Sports and Exercise</li>
</ul>

<section class="abs news"></section>
<div class="abs tweet-bubble"></div>
<svg class="abs tweet-tail" width="40" height="30" viewBox="0 0 40 30"><path d="M0 0 L38 0 L10 28 Z" fill="#2a8a36"/></svg>
<div class="abs tweet-icon"></div>
<h3 class="abs tweet-title">Latest Tweet</h3>
<p class="abs tweet-text">@loremipsum:<br>lorem ipsum dole ri ma<br>sa mdole ri ma sa m do<br>le ri ma sa</p>
<h2 class="abs section-title blog-title">BLOG</h2>
<div class="abs blog-rule"></div>
<p class="abs blog-date">Sunday 21st April, 2010</p>
<p class="abs blog-text">Search interests in the cutting edge areas of biological therapies, most notable stem cells. None of my patients are dying of anything, and most of them come to see me to decrease their pain, so they can get back to what they want to do</p>
<a class="abs more-link blog-more" href="#">Read More
  <svg viewBox="0 0 18 18"><circle cx="9" cy="9" r="9" fill="#fff"/><path d="M7 4.5 11.5 9 7 13.5" stroke="#2f983c" stroke-width="2" fill="none"/></svg>
</a>

<footer class="abs site-footer"></footer>
<a class="abs foot-nav" style="left:166px" href="#">Location</a>
<a class="abs foot-nav" style="left:260px" href="#">Research</a>
<a class="abs foot-nav" style="left:358px" href="#">Blog</a>
<a class="abs foot-nav" style="left:420px" href="#">Sort Me Out</a>
<a class="abs foot-nav" style="left:541px" href="#">Bio</a>
<a class="abs foot-nav" style="left:592px" href="#">Social</a>
<a class="abs foot-nav" style="left:755px" href="#">Terms &amp; Conditions</a>
<a class="abs foot-nav" style="left:938px" href="#">Privacy Policy</a>

</body>
</html>
```